TUMBLAVERA

We are a group of friends with a passion for ancestral knowledge of potions and medicinal formulas derived from nature. We specialise in medicinal mushrooms and adaptogens. We designed a few supplement formulas which we want to release to the market. Our team comes from biology and nutritional science background. Every product we launch will be clean in biodegradable packaging.
Our first product is a lab-tested grass-fed bovine collagen type I, II, and III mixed with organic lab-tested the most potent and bioavailable medicinal mushrooms on the market. This product will be in a pouch the print will be on the pouch or on a label, we don't know if it's possible to design a label that could be used on both? We don't know if we will be able to use organic labels yet due to the legislation changes in the UK. We are waiting for clarification.
The company is called Brindle Cove. We want to use forgotten ancestral knowledge of those potions and reintroduce them to the people. We would like our brand to look clean and friendly. A natural mix of modern and ancestral design.
Our logo and brand designs we like are attached. I have attached the source file of our logo if anyone thinks colours could be different we are open to ideas. I have also attached the visual design we were playing with on canva.com.

```html
<!DOCTYPE html>
<html lang="en">
<head>
<meta charset="utf-8">
<title>TUMBLAVERA – Collagen Peptides &amp; Medicinal Mushrooms</title>
<link rel="stylesheet" href="https://fonts.googleapis.com/css2?family=Open+Sans:wght@300;400;600;700;800&display=swap">
<style>
  :root {
    --backdrop: #ececec;
    --band-dark: #3f3f3f;
    --band-mid: #565656;
    --motif-light: #7a7a7a;
    --label-white: #ffffff;
    --ink: #4a4a4a;
    --ink-strong: #333333;
    --copper: #d4843a;
    --copper-light: #e6a262;
    --rule: #8a8a8a;
  }
  * { box-sizing: border-box; margin: 0; padding: 0; }
  html, body {
    width: 1200px;
    height: 800px;
    overflow: hidden;
    background: var(--backdrop);
    font-family: "Open Sans", Arial, sans-serif;
  }
  .label {
    position: absolute;
    left: 350px;
    top: 30px;
    width: 500px;
    height: 740px;
    background: var(--label-white);
    overflow: hidden;
    box-shadow: 0 6px 24px rgba(0,0,0,0.12);
  }
  .hero-band {
    position: absolute;
    left: 0; top: 0;
    width: 500px;
    height: 345px;
    background: linear-gradient(160deg, var(--band-mid) 0%, var(--band-dark) 100%);
  }
  .mushroom-artwork {
    position: absolute;
    left: 0; top: 0;
    width: 500px;
    height: 260px;
    background:
      radial-gradient(ellipse 130px 90px at 150px 40px, rgba(140,140,140,0.55), transparent 70%),
      radial-gradient(ellipse 80px 80px at 370px 50px, rgba(120,120,120,0.45), transparent 70%),
      radial-gradient(ellipse 60px 110px at 40px 170px, rgba(120,120,120,0.4), transparent 70%),
      radial-gradient(ellipse 60px 120px at 490px 150px, rgba(120,120,120,0.4), transparent 70%);
  }
  .brand-mark {
    position: absolute;
    left: 0; top: 170px;
    width: 500px;
    display: flex;
    justify-content: center;
    align-items: center;
    gap: 8px;
  }
  .brand-mark__square {
    width: 14px; height: 14px;
    background: var(--copper-light);
  }
  .brand-mark__name {
    font-size: 22px;
    font-weight: 600;
    color: var(--copper-light);
  }
  .product-name {
    position: absolute;
    left: 0; top: 255px;
    width: 500px;
    text-align: center;
    font-size: 58px;
    font-weight: 800;
    letter-spacing: 0.5px;
    color: var(--label-white);
    line-height: 1;
  }
  .product-name__accent { color: var(--copper); }
  .formula {
    position: absolute;
    left: 75px; top: 405px;
    font-size: 21px;
    font-weight: 700;
    letter-spacing: 2px;
    color: var(--ink);
    line-height: 31px;
  }
  .formula__ampersand {
    position: absolute;
    left: 343px; top: 355px;
    font-size: 120px;
    font-weight: 800;
    color: var(--copper);
    line-height: 1;
  }
  .collagen-types {
    position: absolute;
    left: 0; top: 515px;
    width: 500px;
    text-align: center;
    font-size: 23px;
    font-weight: 400;
    color: var(--ink-strong);
  }
  .flavour {
    position: absolute;
    left: 0; top: 549px;
    width: 500px;
    text-align: center;
    font-size: 18px;
    font-weight: 300;
    color: var(--copper);
  }
  .divider {
    position: absolute;
    left: 90px; top: 582px;
    width: 322px;
    height: 1px;
    background: var(--rule);
  }
  .category {
    position: absolute;
    left: 0; top: 627px;
    width: 500px;
    text-align: center;
    font-size: 15px;
    font-weight: 400;
    color: var(--copper);
  }
  .pack-facts {
    position: absolute;
    left: 0; top: 656px;
    width: 500px;
    text-align: center;
    font-size: 12px;
    font-weight: 700;
    color: var(--ink-strong);
    line-height: 23px;
  }
</style>
</head>
<body>
  <main class="label">
    <section class="hero-band">
      <div class="mushroom-artwork" role="img" aria-label="Engraved-style drawings of medicinal mushrooms in soft grey tones"></div>
      <div class="brand-mark">
        <span class="brand-mark__square"></span>
        <span class="brand-mark__name">Brindle Cove</span>
      </div>
      <h1 class="product-name">TUMB<span class="product-name__accent">LAVERA</span></h1>
    </section>

    <span class="formula__ampersand">&amp;</span>
    <p class="formula">COLLAGEN PEPTIDES<br>MEDICINAL MUSHROOMS</p>

    <p class="collagen-types">TYPE I, II, III</p>
    <p class="flavour">unflavoured</p>
    <div class="divider"></div>

    <p class="category">FOOD SUPPLEMENT</p>
    <p class="pack-facts">NET WT 360g<br>30 SERVINGS</p>
  </main>
</body>
</html>
```